Form Crafters Business Card

Professional cosmetic surgery company, based in very exclusive area in London. High profiled clientele. Brand is very artistic, modern, state-of-the-art, safe. The best in the business. Celebrity clientele.

Form Crafter’s of London is a brand serving a discriminating and exclusive clientele who value personal service that is both intimate and high end. Our clients choose Form Crafters because of the relationships we share with all of our customers. The clients of Form Crafters have an equal partnership between customers, and very experienced, highly qualified medical professionals. This together provides you with a professional service that keeps you looking good and feeling good. It is a relationship based on honesty, compassion, loyalty and respect.
Form Crafter’s have provided services for internationally recognised celebrities, and other high profiled individuals.

The cards are used for networking at private, exclusive events with VIPs.

Target Market(s)

Professionals
Rich people

Industry/Entity Type

Professional Service

Contact Information for Business Card

Need double sided business card design for 4 people. Back of the business card needs to have contrast background to the front with butterfly watermark with services provided:
Hair Restoration surgery
Hair Loss treatments
Breast surgery
Rhinoplasty
Sonix Liposuction
Fat Grafting
Relaxin & Fillers

Front of the business card needs to be a nice satin black.
with following information:
Tavish Kolendran - name
Chief Executive - Job title

www.formcrafters.co.uk
tavish@formcrafters.co.uk
Phone: +44 (0)207 461 2295
Mobile: +44 (0)7912 548 237

The London Ashcombe Clinic
14 Ashcombe Street | London | W1K 3PQ
Off Tolland Street

All business cards have the same address, phone, website as Tavish's details.
Same details on the back of the business card as well.
The other cards have different name, job title, email, mobile number

Faraz Qureshi - Name
Partner - Job Title
Former England International Cricketer - please include below job title

email: faraz@formcrafters.co.uk
mobile: +44(0)7846 205318

Dr Tadeu Varella - Name
Plastic Surgeon - Job Title
drvarella@formcrafters.co.uk
No mobile number

Dr Zain Hussaini FRCS (please put FRCS in small font) - Name
Hair Restoration Surgeon - Job Title
drhussaini@formcrafters.co.uk
No mobile number

Colors
cedeec
85abd2
0655a3

Requirements
Must have
• The logo needs to be in a metallic finish
• Text needs to be striking
• nice background
• butterfly watermark on the back

```html
<!DOCTYPE html>
<html lang="en">
<head>
<meta charset="utf-8">
<title>Form Crafters Business Card</title>
<link href="https://fonts.googleapis.com/css2?family=Cormorant+Garamond:wght@500;700&family=Arimo:wght@400&display=swap" rel="stylesheet">
<style>
  :root {
    --stage: #5f6166;
    --card-white: #ffffff;
    --card-black: #050505;
    --gold: #f0a31c;
    --blue: #0655a3;
    --blue-bright: #2f6fd6;
    --sky: #85abd2;
    --mist: #cedeec;
    --orange: #f05a14;
    --divider: #6b5330;
  }
  * { box-sizing: border-box; margin: 0; padding: 0; }
  html, body { width: 1200px; height: 960px; overflow: hidden; }
  body {
    background: var(--stage);
    display: flex;
    align-items: center;
    justify-content: center;
    gap: 40px;
  }
  .card {
    width: 540px;
    height: 340px;
    position: relative;
    overflow: hidden;
    box-shadow: 0 10px 30px rgba(0,0,0,0.35);
  }

  /* Services side */
  .card--services { background: var(--card-white); }
  .watermark {
    position: absolute;
    left: 170px; top: 40px;
    width: 230px; height: 260px;
    border-radius: 50% 50% 45% 45%;
    background: radial-gradient(ellipse at center, rgba(133,171,210,0.28), rgba(206,222,236,0.12) 60%, rgba(255,255,255,0) 75%);
  }
  .services-heading {
    position: absolute;
    left: 40px; top: 150px;
    font-family: "Arimo", sans-serif;
    font-weight: 400;
    font-size: 26px;
    color: var(--orange);
  }
  .service-list {
    position: absolute;
    list-style: none;
    font-family: "Arimo", sans-serif;
    font-size: 19px;
    color: var(--blue);
    line-height: 30px;
  }
  .service-list--left { left: 110px; top: 190px; }
  .service-list--right { left: 330px; top: 60px; }
  .service-list li::before {
    content: "\2733";
    color: var(--orange);
    font-size: 14px;
    margin-right: 14px;
  }

  /* Contact side */
  .card--contact {
    background: radial-gradient(ellipse at 60% 40%, #161616, var(--card-black) 70%);
  }
  .brand {
    position: absolute;
    left: 0; top: 0;
    width: 270px; height: 340px;
    display: flex;
    flex-direction: column;
    align-items: center;
    justify-content: center;
    gap: 8px;
  }
  .brand-name {
    display: flex;
    align-items: center;
    gap: 10px;
    font-family: "Cormorant Garamond", serif;
    font-weight: 500;
    font-size: 30px;
    color: var(--gold);
    letter-spacing: 1px;
    text-transform: uppercase;
  }
  .brand-mark {
    width: 12px; height: 12px;
    border-radius: 50%;
    background: var(--gold);
  }
  .brand-tagline {
    font-family: "Arimo", sans-serif;
    font-size: 8px;
    letter-spacing: 1px;
    color: var(--gold);
    text-transform: uppercase;
  }
  .divider {
    position: absolute;
    left: 270px; top: 30px;
    width: 1px; height: 280px;
    background: linear-gradient(var(--card-black), var(--divider), var(--card-black));
  }
  .contact {
    position: absolute;
    left: 280px; top: 52px;
    right: 10px;
    text-align: center;
  }
  .person-name, .clinic-name {
    font-family: "Cormorant Garamond", serif;
    font-weight: 700;
    color: var(--gold);
    white-space: nowrap;
  }
  .person-name { font-size: 26px; line-height: 30px; }
  .clinic-name { font-size: 20px; margin-top: 24px; }
  .person-title {
    font-family: "Cormorant Garamond", serif;
    font-weight: 500;
    font-size: 16px;
    color: var(--blue-bright);
    margin-top: 2px;
  }
  .contact-line {
    font-family: "Arimo", sans-serif;
    font-size: 11.5px;
    color: var(--blue-bright);
    line-height: 17px;
    white-space: nowrap;
  }
  .contact-block { margin-top: 10px; }
</style>
</head>
<body>
  <section class="card card--services">
    <div class="watermark" role="img" aria-label="Faint butterfly watermark"></div>
    <h2 class="services-heading">services :-</h2>
    <ul class="service-list service-list--left">
      <li>Hair Restoration surgery</li>
      <li>Hair Loss treatments</li>
      <li>Breast surgery</li>
      <li>Rhinoplasty</li>
    </ul>
    <ul class="service-list service-list--right">
      <li>Sonix Liposuction</li>
      <li>Fat Grafting</li>
      <li>Relaxin &amp; Fillers</li>
    </ul>
  </section>

  <section class="card card--contact">
    <div class="brand">
      <div class="brand-name"><span class="brand-mark"></span>Form Crafters</div>
      <div class="brand-tagline">Refined care, lasting grace</div>
    </div>
    <div class="divider"></div>
    <div class="contact">
      <div class="person-name">Tavish Kolendran</div>
      <div class="person-title">Chief Executive</div>
      <div class="contact-line">M: +44 (0)7912 548 237</div>
      <div class="clinic-name">The London Ashcombe Clinic</div>
      <div class="contact-block">
        <div class="contact-line">P: +44 (0)207 461 2295</div>
        <div class="contact-line">www.formcrafters.co.uk</div>
        <div class="contact-line">tavish@formcrafters.co.uk</div>
        <div class="contact-line">14 Ashcombe Street | London | W1K 3PQ</div>
        <div class="contact-line">Off Tolland Street</div>
      </div>
    </div>
  </section>
</body>
</html>
```